Tasman Curdworks Guild needs new business cards

We need new business cards designed and produced. We are likely to need other design work done for ads, flyers etc in future.

We would like to start with an initial business card.

The Tasman Curdworks Guild (TCG) is a membership-based not-for-profit organisation that looks after the interests of Australia's small to medium artisan cheesemakers, many of whom are also small-scale farmers. The design should be simple, using our logo, but also communicate our artisan cheese and small dairy farm focus.

The first card to be designed and produced is for me, Miriam Tolhurst. My details are:

Miriam Tolhurst
Secretary
Tasman Curdworks Guild (TCG)
http://www.curdworksguild.example
T +61452837190
E miriam.miriamtolhurst@mailbox.example

I have attached the TCG logo in jpg form. I have a higher resolution version available if needed.

Thank you!

Miriam

Miriam Tolhurst
Tasman Curdworks Guild
miriam.miriamtolhurst@mailbox.example
+61452837190

Sans Serif

• Logo (see attached file)

```html
<!DOCTYPE html>
<html lang="en">
<head>
<meta charset="utf-8">
<title>Miriam Tolhurst — Tasman Curdworks Guild</title>
<link rel="stylesheet" href="https://fonts.googleapis.com/css2?family=Cinzel:wght@400;500&family=Marcellus&display=swap">
<style>
  :root {
    --paper: #ffffff;
    --brown: #5a3818;
    --gold: #c6922c;
    --butter: #f8d46c;
    --butter-soft: #fbe4a0;
    --butter-ring: #fbe3a2;
  }
  html, body {
    margin: 0;
    padding: 0;
    overflow: hidden;
    background: var(--paper);
  }
  .card {
    position: relative;
    width: 1200px;
    height: 688px;
    background: var(--paper);
    overflow: hidden;
    font-family: "Marcellus", Georgia, serif;
    color: var(--brown);
  }
  .artwork {
    position: absolute;
    top: 0;
    right: 0;
    width: 480px;
    height: 688px;
    background: linear-gradient(100deg, var(--butter-soft) 0%, var(--butter) 45%, var(--butter) 100%);
  }
  .identity {
    position: absolute;
    left: 46px;
    top: 84px;
    padding-left: 28px;
    border-left: 12px solid var(--butter);
    height: 125px;
  }
  .identity__name {
    margin: -6px 0 0;
    font-family: "Cinzel", "Times New Roman", serif;
    font-weight: 400;
    font-size: 46px;
    letter-spacing: 0.04em;
    line-height: 1.1;
    color: var(--brown);
  }
  .identity__role {
    margin: 6px 0 0;
    font-family: "Cinzel", "Times New Roman", serif;
    font-size: 28px;
    letter-spacing: 0.48em;
    line-height: 1;
    color: var(--gold);
  }
  .identity__org {
    margin: 8px 0 0;
    font-size: 22px;
    line-height: 1.2;
    color: var(--brown);
    white-space: nowrap;
  }
  .contact-rail {
    position: absolute;
    left: 66px;
    top: 449px;
    width: 4px;
    height: 239px;
    background: var(--butter);
  }
  .contacts {
    position: absolute;
    left: 45px;
    top: 426px;
    margin: 0;
    padding: 0;
    list-style: none;
  }
  .contact {
    display: flex;
    align-items: center;
    height: 46px;
    margin-bottom: 19px;
  }
  .contact__icon {
    flex: none;
    width: 46px;
    height: 46px;
  }
  .contact__text {
    margin-left: 13px;
    font-size: 25px;
    letter-spacing: 0.03em;
    color: var(--brown);
  }
</style>
</head>
<body>
<main class="card">
  <div class="artwork" role="img" aria-label="Illustration of a yellow cheese wedge with holes, framed by a brown brush-stroke arc"></div>

  <header class="identity">
    <h1 class="identity__name">Miriam Tolhurst</h1>
    <p class="identity__role">Secretary</p>
    <p class="identity__org">Tasman Curdworks Guild (TCG)</p>
  </header>

  <div class="contact-rail"></div>

  <ul class="contacts">
    <li class="contact">
      <svg class="contact__icon" viewBox="0 0 46 46" aria-hidden="true">
        <circle cx="23" cy="23" r="21.5" fill="var(--butter)" stroke="var(--butter-ring)" stroke-width="3"/>
        <path d="M15 13.5c1.5-1.5 3-1.5 4 0l2.2 3.4c.7 1.1.4 2.3-.6 3l-1.4 1c1 2.6 3.2 5 5.9 6.1l1-1.4c.7-1 2-1.3 3-.6l3.4 2.2c1.5 1 1.5 2.5 0 4l-1.6 1.6c-1.7 1.7-5 1.2-9-1.6-3.6-2.5-6.4-5.9-7.9-9.3-1.3-3-1.2-5.5.4-7z" fill="none" stroke="var(--brown)" stroke-width="1.6" stroke-linejoin="round"/>
      </svg>
      <span class="contact__text">+6 145 283 7190</span>
    </li>
    <li class="contact">
      <svg class="contact__icon" viewBox="0 0 46 46" aria-hidden="true">
        <circle cx="23" cy="23" r="21.5" fill="var(--butter)" stroke="var(--butter-ring)" stroke-width="3"/>
        <rect x="11.5" y="15" width="23" height="16" fill="none" stroke="var(--brown)" stroke-width="1.6"/>
        <path d="M11.5 15l11.5 9 11.5-9M11.5 31l8.5-8M34.5 31l-8.5-8" fill="none" stroke="var(--brown)" stroke-width="1.6"/>
      </svg>
      <span class="contact__text">miriam.miriamtolhurst@mailbox.example</span>
    </li>
    <li class="contact">
      <svg class="contact__icon" viewBox="0 0 46 46" aria-hidden="true">
        <circle cx="23" cy="23" r="21.5" fill="var(--butter)" stroke="var(--butter-ring)" stroke-width="3"/>
        <g fill="none" stroke="var(--brown)" stroke-width="1.5">
          <circle cx="23" cy="23" r="11"/>
          <ellipse cx="23" cy="23" rx="5" ry="11"/>
          <path d="M12 23h22M13.5 17.5h19M13.5 28.5h19M23 12v22"/>
        </g>
      </svg>
      <span class="contact__text">www.curdworksguild.example</span>
    </li>
  </ul>
</main>
</body>
</html>
```